Financial Sevices firm looking for Brochure design

Our company Veltmoor Capital and Holdings Limited (VeltHoldings)
i
Is an investment/advisory firm - www.veltholdings-grp.net
We invest in the energy sector in Africa and offer advisory services to Energy companies looking to invest in Africa. From oil and gas, to renewables (wind/solar). We are more focused on the "West African" Sub region
We need corporate brochure (Booklet style) to circulate to our corporate clients
We would like to see a design that considers the colours in our Logo (see website)
HI Guys, sorry been travelling. Seen some very good submissions and will be sending updates shortly
Reason: Dear Designers,
Thank you for participating in this project and for some of the great designs i've received so far. Unfortunately, due to the holidays, it has been difficult to consult with other members of my team. As a result, the project deadline is extended by about 12 days
I appreciate your understanding in the situation and looking forward to continuing the excellent collaboration in the coming days
Reason: Hi All,
Apologies for the multiple deadline extensions and thanks so much for all the designs which my team and I will be reviewing today and tomorrow.
We will be closing this project tomorrow by 6pm GMT (17th Jan 2014)
Thanks to all those that submitted such wonderful designs and goodluck!!
Project to be closed finally on 17th Jan 2014 at 6pm GMT
Banks, Investment Firms, Energy companies, Private Equity Funds
I have attached a Brochure that I created myself as an example of the type of information required but please also feel free to visit our website www.veltholdings-grp.net
Looking for any creative ideas you have to suplement the information provided.
Financial

```html
<!DOCTYPE html>
<html lang="en">
<head>
<meta charset="utf-8">
<title>Veltmoor Capital and Holdings Limited – Corporate Profile</title>
<link rel="stylesheet" href="https://fonts.googleapis.com/css2?family=Roboto+Slab:wght@300;400;700&display=swap">
<style>
  :root {
    --page-bg: #e4e4e4;
    --cover-red: #b7202a;
    --cover-red-light: #c8323a;
    --cover-red-dark: #a11a24;
    --frame-white: #f4f4f4;
    --band-white: #f7f7f7;
    --brand-red: #b7202a;
    --text-light: #f3f3f3;
  }
  * { box-sizing: border-box; margin: 0; padding: 0; }
  html, body {
    width: 1200px;
    height: 800px;
    overflow: hidden;
    background: var(--page-bg);
    font-family: "Roboto Slab", Georgia, serif;
  }
  .cover {
    position: absolute;
    left: 120px;
    top: 60px;
    width: 960px;
    height: 680px;
    background: linear-gradient(160deg, var(--cover-red-light) 0%, var(--cover-red) 45%, var(--cover-red-dark) 100%);
    box-shadow: 0 6px 18px rgba(0,0,0,0.18);
    overflow: hidden;
  }
  .photo {
    position: absolute;
    border-radius: 26px;
    border: 2px solid var(--frame-white);
  }
  .photo--oil-field {
    left: 70px; top: 110px; width: 250px; height: 200px;
    background: linear-gradient(180deg, #b7cde6 0%, #d9e3ea 45%, #5f7d3e 70%, #3b4a2a 100%);
  }
  .photo--water-pump {
    left: 345px; top: 70px; width: 300px; height: 200px;
    background: linear-gradient(120deg, #9a9a96 0%, #b9b3ad 40%, #c98a96 60%, #5a5650 100%);
  }
  .photo--infrastructure {
    left: 70px; top: 335px; width: 280px; height: 215px;
    background: linear-gradient(170deg, #2e58b8 0%, #6f8fd0 30%, #d7a12a 55%, #8a5a12 100%);
  }
  .title {
    position: absolute;
    left: 690px;
    top: 60px;
    transform-origin: left top;
    transform: rotate(90deg) translateY(-100%);
    color: var(--text-light);
    white-space: nowrap;
    display: flex;
    flex-direction: column;
    line-height: 1;
  }
  .title__light { font-weight: 300; font-size: 46px; }
  .title__bold  { font-weight: 700; font-size: 46px; margin-top: 4px; }
  .brand-band {
    position: absolute;
    right: 0;
    top: 520px;
    width: 420px;
    height: 90px;
    background: var(--band-white);
    display: flex;
    align-items: center;
    gap: 12px;
    padding-left: 36px;
  }
  .brand-band__mark {
    width: 28px; height: 28px;
    background: var(--brand-red);
  }
  .brand-band__name {
    font-family: "Roboto Slab", Georgia, serif;
    font-weight: 400;
    font-size: 34px;
    color: var(--brand-red);
    letter-spacing: 0.5px;
  }
</style>
</head>
<body>
  <main class="cover">
    <div class="photo photo--oil-field" role="img" aria-label="Photograph of an oil pumpjack on green farmland under a blue sky"></div>
    <div class="photo photo--water-pump" role="img" aria-label="Photograph of a child collecting water from a village hand pump"></div>
    <div class="photo photo--infrastructure" role="img" aria-label="Photograph of a steel construction frame and crane lit in golden light"></div>

    <h1 class="title">
      <span class="title__light">Corporate</span>
      <span class="title__bold">Profile</span>
    </h1>

    <div class="brand-band">
      <span class="brand-band__mark"></span>
      <span class="brand-band__name">VeltHoldings</span>
    </div>
  </main>
</body>
</html>
```